Very Simple Web Redesign Project - Using Photoshop

Required is a very simple website home page redesign for the following site: http://www.tallowcrestslate.com.au/
I require this as a Photoshop design.
The basic look and feel of the site needs to remain.
Specifically the colours don't need to be changed.
The positioning of the site is currently correct for the target market.
The site does not need to be made super slick looking. Just upgraded to a new version.
The current text can all be used.
The only menus necessary are a horizontal menu at the top, and a simple horizontal text menu at the bottom of the page. Do NOT retain the vertical menu on the home page (having the items "Our Gallery", "Our Services", "Enquire Now").
Give the horizontal menu the following items:
Home | Slate Roof Repairs | Slate Reroofing | Slate Roof Benefits | Other Services | Photo Gallery | FAQ's | Free Quote | Contact Us
The picture of the house at the top RHS of the page needs to be reduced in size by approx 50% and moved to the top LHS of the page.
Please place the following text into the top of the page:
"Call Now: 0427 618 392"
Keep the four pictures on the home page layout. Some larger images attached.
Thanks,
Rob
Updates
Hi,
Thanks for all the designs.
I am working with my client to get which one they like the most.
Thanks,
Rob

```html
<!DOCTYPE html>
<html lang="en">
<head>
<meta charset="utf-8">
<title>Tallowcrest Slate – Slate Roof Specialists</title>
<link href="https://fonts.googleapis.com/css2?family=Source+Sans+3:wght@400;600;700&family=Arimo:wght@400;700&display=swap" rel="stylesheet">
<style>
:root{
  --green-dark:#2f8a12;
  --green-mid:#4aa41c;
  --green-light:#8fd05a;
  --green-text:#3a9a14;
  --green-btn:#127a0c;
  --footer:#0b7a0b;
  --footer-line:#5cb43a;
  --ink:#222;
  --body:#555;
  --red:#9a1a1a;
  --slate:#8f8d96;
  --white:#fff;
}
*{margin:0;padding:0;box-sizing:border-box}
html,body{width:1100px;height:1200px;overflow:hidden}
body{position:relative;background:var(--white);font-family:"Arimo",Arial,sans-serif;color:var(--body)}
.hero-bg{position:absolute;left:0;top:0;width:1100px;height:447px;
  background:radial-gradient(ellipse at 55% 10%,#5cb427 0%,#3f981a 50%,#2f8212 100%)}
.hero-edge{position:absolute;left:0;top:447px;width:1100px;height:6px;background:#8ccc5e}
.logo{position:absolute;left:92px;top:18px;width:363px;height:76px;background:var(--white);border-radius:6px;
  box-shadow:0 3px 8px rgba(0,0,0,.3);display:flex;align-items:center;padding-left:18px;gap:14px}
.logo-mark{width:40px;height:40px;background:var(--green-dark)}
.logo-name{font-family:"Source Sans 3",sans-serif;font-weight:700;font-size:32px;color:var(--green-dark)}
.call-now{position:absolute;right:74px;top:47px;font-family:"Source Sans 3",sans-serif;font-size:22px;font-weight:600;color:var(--white)}
.main-nav{position:absolute;left:74px;top:121px;width:952px;height:53px;border-radius:5px;
  background:linear-gradient(#fff 0%,#fff 55%,#e6e6e6 100%);box-shadow:0 2px 6px rgba(0,0,0,.3);display:flex;overflow:hidden}
.main-nav a{display:flex;align-items:center;justify-content:center;height:100%;font-size:14px;color:#333;text-decoration:none;border-right:1px solid #ddd}
.main-nav a:last-child{border-right:0}
.main-nav a.active{background:linear-gradient(#e9f7dc,#a8e07c)}
.slider-shadow{position:absolute;left:74px;top:200px;width:952px;height:345px;border-radius:50%/8%;
  background:linear-gradient(#d8d8d8,#f4f4f4);box-shadow:0 8px 10px rgba(0,0,0,.12)}
.slider{position:absolute;left:92px;top:196px;width:918px;height:341px;border:1px solid #ccc;overflow:hidden}
.slide-photo{position:absolute;inset:0;background:linear-gradient(160deg,#b8b4ad 0%,#9a98a0 35%,#7e7c86 70%,#57555c 100%)}
.slide-arrow{position:absolute;top:140px;width:58px;height:58px;background:rgba(30,30,30,.85);display:flex;align-items:center;justify-content:center}
.slide-arrow.prev{left:27px}.slide-arrow.next{left:829px}
.slide-caption{position:absolute;left:0;bottom:0;width:100%;height:66px;background:rgba(35,35,35,.88);
  font-family:"Source Sans 3",sans-serif;font-size:21px;color:var(--white);padding:20px 0 0 22px}
.slide-caption em{font-style:normal;color:var(--green-light)}
.slide-dots{position:absolute;right:37px;top:26px;display:flex;gap:16px}
.slide-dots span{width:17px;height:17px;border-radius:50%;background:var(--white)}
.slide-dots span.on{background:#5cc02a;box-shadow:0 0 0 2px #ddd}
h2{font-family:"Source Sans 3",sans-serif;font-weight:400;font-size:20px;color:var(--ink);position:absolute}
.photo{border:2px solid #777;border-radius:4px;position:absolute}
.text{font-size:12.5px;line-height:20px;position:absolute}
.text .red{color:var(--red)}
.text .grn{color:var(--green-text)}
.view-more{position:absolute;left:654px;top:719px;font-size:12.5px;color:#333;text-decoration:underline}
.work-card{position:absolute;top:812px;width:212px;height:240px;border-radius:4px;background:linear-gradient(#fff 0%,#f6f6f6 45%,#e4e4e4 100%)}
.work-card .photo{left:16px;top:3px;width:177px;height:100px}
.work-card h3{position:absolute;left:13px;top:112px;font-weight:400;font-size:12.5px;color:#111}
.work-card p{position:absolute;left:13px;top:134px;width:190px;font-size:12.5px;line-height:18px}
.work-card p .red{color:var(--red)}
.btn{position:absolute;left:120px;top:202px;width:79px;height:23px;border-radius:5px;background:var(--btn,var(--green-btn));
  color:var(--white);font-size:11px;display:flex;align-items:center;justify-content:center}
.divider{position:absolute;left:740px;top:572px;height:480px;border-left:2px dotted #bbb}
.quote-head{left:753px;top:569px;line-height:24px}
.quote-head span{color:var(--green-text)}
.quote-btn{position:absolute;left:763px;top:732px;width:190px;height:60px;border-radius:4px;
  background:linear-gradient(#a6d84a,#5ba81e);box-shadow:0 2px 3px rgba(0,0,0,.3);
  font-family:"Source Sans 3",sans-serif;font-weight:600;font-size:19px;color:var(--white);padding:19px 0 0 17px;letter-spacing:-.3px}
.quote-house{position:absolute;left:937px;top:722px;width:72px;height:76px;background:linear-gradient(#6a8fb8,#e8eef2)}
.contact-list{position:absolute;left:757px;top:884px;font-size:12.5px;color:#444}
.contact-list .row{display:flex;margin-bottom:10px;line-height:20px}
.contact-list .label{width:63px;text-align:right;padding-right:10px;white-space:nowrap}
.footer{position:absolute;left:0;top:1078px;width:1100px;height:122px;background:var(--footer);border-top:6px solid var(--footer-line)}
.footer-nav{position:absolute;left:0;top:26px;width:100%;text-align:center;font-size:11px;font-weight:700;color:var(--white)}
.footer-nav a{color:var(--white);text-decoration:none}
.footer-nav i{font-style:normal;margin:0 9px}
.copyright{position:absolute;left:76px;top:75px;font-size:11px;color:var(--white)}
.connect{position:absolute;left:752px;top:69px;display:flex;align-items:center;gap:15px;font-size:11px;color:var(--white)}
.connect .social{width:25px;height:24px;border-radius:3px;background:#d9ecd0}
</style>
</head>
<body>
<div class="hero-bg"></div>
<div class="hero-edge"></div>

<header>
  <div class="logo"><span class="logo-mark"></span><span class="logo-name">Tallowcrest Slate</span></div>
  <div class="call-now">Call Now: 0427 618 392</div>
  <nav class="main-nav">
    <a class="active" style="width:69px">Home</a>
    <a style="width:141px">Slate Roof Repairs</a>
    <a style="width:118px">Slate Reroofing</a>
    <a style="width:144px">Slate Roof Benefits</a>
    <a style="width:116px">Other Services</a>
    <a style="width:107px">Photo Gallery</a>
    <a style="width:62px">FAQ's</a>
    <a style="width:94px">Free Quote</a>
    <a style="width:101px">Contact Us</a>
  </nav>
</header>

<div class="slider-shadow"></div>
<section class="slider">
  <div class="slide-photo" role="img" aria-label="Grey slate roof beside a cream dormer window with green frame"></div>
  <div class="slide-arrow prev"><svg width="18" height="26" viewBox="0 0 18 26"><path d="M14 3 L5 13 L14 23" fill="none" stroke="#ccc" stroke-width="4"/></svg></div>
  <div class="slide-arrow next"><svg width="18" height="26" viewBox="0 0 18 26"><path d="M4 3 L13 13 L4 23" fill="none" stroke="#ccc" stroke-width="4"/></svg></div>
  <div class="slide-caption"><em>Tallowcrest Slate</em> - the Slate Roof Specialists
    <div class="slide-dots"><span class="on"></span><span></span><span></span><span></span><span></span></div>
  </div>
</section>

<main>
  <h2 style="left:74px;top:568px">Welcome To Our Site</h2>
  <div class="photo" style="left:74px;top:606px;width:178px;height:128px;background:linear-gradient(#7fa4cc,#5c6a62 60%,#dcdcd6)" role="img" aria-label="Heritage house with slate roof and white gable"></div>
  <div class="text" style="left:274px;top:601px;width:440px">
    <p class="red" style="margin-bottom:8px">The standard chunk of Lorem Ipsum used since the 1500s is reproduced below for those interested.</p>
    <p>Sections 1.10.32 and 1.10.33 from <span class="grn">"de Finibus Bonorum et Malorum"</span> by Cicero are also reproduced in their exact original form, accompanied by English versions from the 1914 translation by H. Rackham.</p>
  </div>
  <a class="view-more">View more</a>

  <h2 style="left:74px;top:768px">Our Works</h2>
  <article class="work-card" style="left:74px">
    <div class="photo" role="img" aria-label="Octagonal slate roofed gazebo among trees" style="background:linear-gradient(#4f7a3a,#8a8a86 45%,#c9b98a 80%,#4f7a3a)"></div>
    <h3>"de Finibus Bonorum et Malorum"</h3>
    <p><span class="red">Cicero are also reproduced</span> in their exact original form, accompanied by English versions</p>
    <span class="btn">View more</span>
  </article>
  <article class="work-card" style="left:296px">
    <div class="photo" role="img" aria-label="Flat slate roof beside brick wall" style="background:linear-gradient(#8a5a48,#8e8c90 35%,#a3a1a6)"></div>
    <h3>"de Finibus Bonorum et Malorum"</h3>
    <p><span class="red">Cicero are also reproduced</span> in their exact original form, accompanied by English versions</p>
    <span class="btn">View more</span>
  </article>
  <article class="work-card" style="left:517px">
    <div class="photo" role="img" aria-label="Dark slate roof with cream dormer" style="background:linear-gradient(135deg,#5a5866,#4a4856 50%,#b69a7a)"></div>
    <h3>"de Finibus Bonorum et Malorum"</h3>
    <p><span class="red">Cicero are also reproduced</span> in their exact original form, accompanied by English versions</p>
    <span class="btn">View more</span>
  </article>

  <div class="divider"></div>

  <aside>
    <h2 class="quote-head">Call now and arrange a<br><span>free quote:</span></h2>
    <p class="text" style="left:753px;top:631px;width:280px">We service all inner city suburbs of Sydney roughly covering an area encompassing Gordon to Epping, Mosman to Bondi, Coogee to Kogarah and Kings-grove to Burwood and Concord</p>
    <div class="quote-btn">GET A FREE QUOTE</div>
    <div class="quote-house" role="img" aria-label="Small house with blue roof"></div>

    <h2 style="left:753px;top:843px">Contact Us:</h2>
    <div class="contact-list">
      <div class="row"><span class="label">Address :</span><span>14/208 Harcourt Rd<br>Ultimo NSW</span></div>
      <div class="row"><span class="label">Phone :</span><span>0427618392</span></div>
      <div class="row"><span class="label">Fax :</span><span>02 81554620</span></div>
      <div class="row"><span class="label">E - mail :</span><span>sam@tallowcrestslate.com.au</span></div>
    </div>
  </aside>
</main>

<footer class="footer">
  <nav class="footer-nav">
    <a>Home</a><i>|</i><a>Slate Roof Repairs</a><i>|</i><a>Slate Reroofing</a><i>|</i><a>Slate Roof Benefits</a><i>|</i><a>Other Services</a><i>|</i><a>Photo Gallery</a><i>|</i><a>FAQ's</a><i>|</i><a>Free Quote</a><i>|</i><a>Contact Us</a><i>|</i><a>Sitemap</a>
  </nav>
  <p class="copyright">Copyright © 2011 www.tallowcrestslate.com.au All rights reserved</p>
  <div class="connect">Connect with us :
    <span class="social"></span><span class="social"></span><span class="social"></span><span class="social"></span><span class="social"></span>
  </div>
</footer>
</body>
</html>
```